Business Card Professional Clean - Ledgerpeak

Create a business card for my company that deals with Cryptocurrencies. I have a few designs ideas that I'd like to be implemented. Thanks! I will include the logo files, and a link to the design styles that I like.

Target Market(s)

Professionals

Industry/Entity Type

Consulting

Contact Information for Business Card

Name: Mark Dunn
Title: CEO/Technical Director
Phone: (587)430-9158
E-mail: mdunn@ledgerpeak.example
Address: Suite 512, 208-3375 Harwood Lane NW

Twitter: @LedgerPeakYYC
Instagram: ledgerpeakyyc

Colors
92b5d7
3276b5
33a6d7
85acd3
85cae6
0592cd

Requirements
Must have
• Some colors that match with the logo and the pictures I put in below.
• Ideally the finished product would look something like the attachments showing the color gradient I want.
Nice to have
• Please see some of the attachments I've included. This is very close to the final product that I would like to see. If someone could recreate something like those I would definitely feel pretty good about it.
• For the instagram and twitter please use the symbols/icon to represent it on the card.
Should not have
• No crazy colors and unprofessional styles. I just want clear info. Don't go outside the boundaries of the colors in the attachment and we should be good. No crazy weird fonts either.

```html
<!DOCTYPE html>
<html lang="en">
<head>
<meta charset="utf-8">
<title>Ledgerpeak Business Card</title>
<link rel="stylesheet" href="https://fonts.googleapis.com/css2?family=Cinzel:wght@400&family=Marcellus&family=Arimo:wght@400&display=swap">
<style>
  :root {
    --paper: #ffffff;
    --card: #070505;
    --brand-blue: #1a5c9c;
    --slate: #3a4c5c;
    --band-deep: #1669a6;
    --band-cyan: #0592cd;
    --band-light: #6aaecb;
    --band-pale: #85c4dd;
    --ink-light: #ffffff;
  }
  * { margin: 0; padding: 0; box-sizing: border-box; }
  html, body {
    width: 951px; height: 1200px; overflow: hidden;
    background: var(--paper);
  }
  .sheet { position: relative; width: 951px; height: 1200px; }
  .card {
    position: absolute; left: 32px; width: 890px; height: 538px;
    background: var(--card); border-radius: 46px; overflow: hidden;
  }
  .card--front { top: 37px; }
  .card--back { top: 628px; }

  .front-band { position: absolute; left: 0; top: 157px; }
  .front-wordmark {
    position: absolute; left: 405px; top: 222px;
    font-family: "Cinzel", serif; font-size: 66px; line-height: 1;
    color: var(--brand-blue); letter-spacing: 1px;
  }

  .back-wordmark {
    position: absolute; right: 40px; top: 132px;
    font-family: "Cinzel", serif; font-size: 22px; line-height: 1;
    color: var(--brand-blue);
  }
  .person {
    position: absolute; left: 0; width: 890px; top: 170px;
    text-align: center; font-family: "Marcellus", serif;
    transform: translateX(-8px);
  }
  .person__name {
    font-size: 84px; line-height: 1; letter-spacing: 1px;
    color: var(--brand-blue); font-weight: 400;
  }
  .person__name .surname { color: var(--slate); }
  .person__title {
    margin-top: 8px; font-size: 38px; line-height: 1;
    color: var(--brand-blue); font-weight: 400;
  }
  .person__title .tail { color: var(--slate); }

  .contact-band { position: absolute; left: 0; bottom: 0; width: 890px; height: 199px; }
  .contact-band svg.stripes { position: absolute; inset: 0; }
  .contact-list, .social-list {
    position: absolute; top: 44px; list-style: none;
    font-family: "Arimo", Arial, sans-serif; font-size: 20px; color: var(--ink-light);
  }
  .contact-list { left: 50px; }
  .social-list { right: 40px; text-align: right; }
  .contact-list li, .social-list li {
    height: 42px; display: flex; align-items: center; gap: 12px;
  }
  .social-list li { justify-content: flex-end; }
  .icon { width: 24px; height: 24px; flex: none; }
  .at-mark { width: 24px; text-align: center; font-size: 23px; font-weight: 400; }
</style>
</head>
<body>
<div class="sheet">

  <section class="card card--front">
    <svg class="front-band" width="160" height="226" viewBox="0 0 160 226" aria-hidden="true">
      <polygon points="0,0 160,0 55,110 0,110" fill="var(--band-cyan)"/>
      <polygon points="0,110 55,110 0,165" fill="var(--band-cyan)"/>
      <polygon points="0,165 55,110 160,0 160,226 0,226" fill="var(--band-deep)"/>
    </svg>
    <div class="front-wordmark">Ledgerpeak</div>
  </section>

  <section class="card card--back">
    <div class="back-wordmark">Ledgerpeak</div>

    <div class="person">
      <h1 class="person__name">MARK <span class="surname">DUNN</span></h1>
      <p class="person__title">CEO/Technical <span class="tail">Director</span></p>
    </div>

    <div class="contact-band">
      <svg class="stripes" width="890" height="199" viewBox="0 0 890 199" aria-hidden="true">
        <rect width="890" height="199" fill="var(--band-deep)"/>
        <polygon points="312,0 517,0 318,199 113,199" fill="var(--band-light)"/>
        <polygon points="517,0 743,0 544,199 318,199" fill="var(--band-cyan)"/>
        <polygon points="743,0 890,0 890,20 711,199 544,199" fill="var(--band-light)"/>
        <polygon points="890,20 890,199 711,199" fill="var(--band-cyan)"/>
      </svg>

      <ul class="contact-list">
        <li>
          <svg class="icon" viewBox="0 0 24 24" aria-hidden="true"><path d="M8 3 L10 7 L8.5 9 Q10 14 14.5 16 L16.5 14.5 L20 16.5 L18.5 20.5 Q10 20 5.5 12 Q3.5 7 5 4 Z" fill="none" stroke="#fff" stroke-width="1.6" stroke-linejoin="round"/></svg>
          <span>(587)430-9158</span>
        </li>
        <li>
          <span class="at-mark">@</span>
          <span>mdunn@ledgerpeak.example</span>
        </li>
        <li>
          <svg class="icon" viewBox="0 0 24 24" aria-hidden="true"><path d="M3 12 L12 3.5 L21 12 M5.5 10 V20.5 H10 V14.5 H14 V20.5 H18.5 V10" fill="none" stroke="#fff" stroke-width="1.7" stroke-linejoin="round"/></svg>
          <span>Suite 512, 208-3375 Harwood Lane NW</span>
        </li>
      </ul>

      <ul class="social-list">
        <li>
          <span>@LedgerPeakYYC</span>
          <svg class="icon" viewBox="0 0 24 24" aria-hidden="true"><circle cx="12" cy="12" r="9" fill="none" stroke="#fff" stroke-width="1.7"/></svg>
        </li>
        <li></li>
        <li>
          <span>@ledgerpeakyyc</span>
          <svg class="icon" viewBox="0 0 24 24" aria-hidden="true"><rect x="3" y="3" width="18" height="18" rx="4" fill="none" stroke="#fff" stroke-width="1.7"/></svg>
        </li>
      </ul>
    </div>
  </section>

</div>
</body>
</html>
```